Business Card Design - Construction Company

Tarrowin Construction is in need of a sharp, modern business card design that has an architectural/high fashion feel.

We are looking for a two sided card.

One side simple dark grey/black with some texture in the background. e.g. (a mosaic of simple interconnecting shapes or a shadow of the logo.) Something to draw attention and create interest.It will need to feature a large Tarrowin construction logo (files attached) in metallic gradient or plain white.

The other side should contain all of our information:

(in largest text)
Name of person
Tarrowin Construction Pty. Ltd.

Licensed builders specialising in:
- Bathrooms
- Kitchens
- Commercial interiors

(mid sized text)
Phone number
Fax number
person@tarrowinconstruction.example.au
www. tarrowinconstruction.example.au

(smaller text)
ABN: 62407938215
BSA license: xxx-xxxx
PO Box 8641 Kellsmoor QLD 4019 (address)

Target Market(s)

professional home and business owners

Industry/Entity Type

Construction

Requirements
Must have
• Must be bold, professional looking and modern.
Nice to have
• We are undecided as to what kind of printing we will go with.
Definitely square edged.
Probably high quality satin card.
We are also interested in designs that would work well on transparent or translucent plastic.
Ideally we would print two versions.
Should not have
• Nothing with an antique feel.
No wild colours. Small amounts of colour can be good in the right place.

```html
<!DOCTYPE html>
<html lang="en">
<head>
<meta charset="utf-8">
<title>Tarrowin Construction – Business Card</title>
<link rel="stylesheet" href="https://fonts.googleapis.com/css2?family=Source+Sans+3:wght@400;600&display=swap">
<style>
  :root {
    --page: #ffffff;
    --card-dark: #231f20;
    --glow-blue: #0d4a9e;
    --glow-mid: #0a2f63;
    --text-light: #f2f2f2;
    --mark-slate: #34445f;
    --mark-steel: #6f747c;
    --texture-a: rgba(255,255,255,0.035);
    --texture-b: rgba(60,90,140,0.10);
  }
  * { margin: 0; padding: 0; box-sizing: border-box; }
  html, body {
    width: 1200px;
    height: 900px;
    overflow: hidden;
    background: var(--page);
    font-family: "Source Sans 3", sans-serif;
  }
  .card {
    position: absolute;
    top: 279px;
    width: 490px;
    height: 317px;
    overflow: hidden;
    background:
      radial-gradient(ellipse 70% 55% at 50% 112%, var(--glow-blue) 0%, var(--glow-mid) 40%, rgba(35,31,32,0) 100%),
      var(--card-dark);
    color: var(--text-light);
  }
  .card--info { left: 27px; }
  .card--brand { left: 687px; }

  .card-texture {
    position: absolute;
    inset: 0;
    background:
      radial-gradient(ellipse 55% 60% at 50% 45%, var(--texture-b) 0%, rgba(0,0,0,0) 70%),
      linear-gradient(135deg, var(--texture-a) 0%, rgba(0,0,0,0) 45%, var(--texture-a) 100%);
  }

  .identity {
    position: absolute;
    left: 15px;
    top: 11px;
    font-size: 21px;
    line-height: 28px;
    text-shadow: 0 0 6px rgba(255,255,255,0.35);
  }
  .services {
    position: absolute;
    left: 15px;
    top: 85px;
    font-size: 17px;
    line-height: 20.8px;
    text-shadow: 0 0 5px rgba(255,255,255,0.3);
  }
  .services ul { list-style: none; }
  .contact {
    position: absolute;
    right: 18px;
    top: 179px;
    text-align: right;
    font-size: 15.5px;
    line-height: 18.8px;
    text-shadow: 0 0 5px rgba(255,255,255,0.3);
  }
  .legal {
    position: absolute;
    right: 18px;
    top: 265px;
    text-align: right;
    font-size: 10px;
    line-height: 13px;
  }
  .brand-watermark {
    position: absolute;
    right: 16px;
    top: 108px;
    font-size: 60px;
    font-weight: 600;
    color: var(--mark-slate);
    line-height: 1;
  }
  .brand-lockup {
    position: absolute;
    left: 0;
    right: 0;
    top: 34px;
    display: flex;
    flex-direction: column;
    align-items: center;
    gap: 16px;
  }
  .brand-lockup svg { display: block; }
  .brand-name {
    font-size: 34px;
    font-weight: 600;
    color: var(--mark-steel);
    line-height: 1;
  }
</style>
</head>
<body>
  <section class="card card--info">
    <div class="card-texture"></div>
    <div class="brand-watermark">Tarrowin</div>
    <div class="identity">
      <p>Name of person</p>
      <p>Tarrowin Construction Pty. Ltd.</p>
    </div>
    <div class="services">
      <p>Licensed builders specialising in:</p>
      <ul>
        <li>- Bathrooms</li>
        <li>- Kitchens</li>
        <li>- Commercial interiors</li>
      </ul>
    </div>
    <div class="contact">
      <p>Phone number</p>
      <p>Fax number</p>
      <p>person@tarrowinconstruction.example.au</p>
      <p>www. tarrowinconstruction.example.au</p>
    </div>
    <div class="legal">
      <p>ABN: 62407938215</p>
      <p>BSA license: xxx-xxxx</p>
      <p>PO Box 8641 Kellsmoor QLD 4019 (address)</p>
    </div>
  </section>

  <section class="card card--brand">
    <div class="card-texture"></div>
    <div class="brand-lockup">
      <svg width="180" height="180" viewBox="0 0 180 180" aria-hidden="true">
        <circle cx="90" cy="90" r="80" fill="none" stroke="#6f747c" stroke-width="16"/>
      </svg>
      <span class="brand-name">Tarrowin Construction</span>
    </div>
  </section>
</body>
</html>
```